PowerPoint template for large technology company

Requesting proposals for a PowerPoint deck template that can be used by our sales team when pitching clients. We are a large technology media company, that is BtoB focused, and are looking for a professional, clean, tech-forward, design and layout. However, our clients are advertisers and brands who would respond well to a subtly stylized creative design.

We need a fully built-out template wherein our sales team can choose from a variety of slide layouts while compiling their pitch decks.

Key objective: To create a template that mandates consistent fonts, sizes, and layout, and is easy to use for novice presenters. A plug-and-play template.

Secondary objective: A refresh on current design of company template.

Presentation template should include:
2 Presentation title slide options
2 Section header options
6 information layout slide options
3 data charts (pie, bar, and column)
Summary/ Thank you slide

The teams using this template will not be adept with PowerPoint but should easily be able to insert images and text boxes without it ruining the design and format of the presentation. The idea is if 20 people use our template to build pitch-decks, all of the individual decks should all look like they came from the same team. Please be as detailed and specific as possible when building out slides.

Simple, high-compatibility fonts. Please see brand guidelines attached.

Target Market(s)

Large advertising agencies and major consumer technology brands.

This deck template will not be consumer facing.

Industry/Entity Type

Building

Font styles to use
Serif
Sans Serif

Requirements
Must have
• Must be clean, high-tech, and forces user to stay within template guidelines during modifications.

Template should be built out for a sales presentation that will be a tool for ppt novices.
Nice to have
• As we are revamping existing decks, it will be nice to see multiple ideas on the design. Think professional, high-tech, and powerful.
Should not have
• Should not have a distracting background that will interfere with presentations or where it will be difficult to easily insert images.

Blacked out backgrounds cause a "boxed in" look for images and/or text boxes - which is undesirable. Either don't include color-blocked backgrounds or introduce a way in which this can be used that avoids the previously stated pitfall.

No rotated text-fill options. (i.e. rotating text by 90 or 180 degrees)

Please don't be too literal in your design approach.

```html
<!DOCTYPE html>
<html lang="en">
<head>
<meta charset="utf-8">
<title>Arcline Presentation Template</title>
<link href="https://fonts.googleapis.com/css2?family=Source+Sans+3:wght@400;600;700&display=swap" rel="stylesheet">
<style>
:root{
  --stage:#000;
  --paper:#fff;
  --paper-tint:#eef2f7;
  --brand:#2d62b0;
  --brand-deep:#1a4690;
  --brand-light:#5b93d6;
  --title:#4a7cc0;
  --ink:#333a44;
  --muted:#7c8794;
  --accent:#f2d21c;
  --bullet:#9cc33c;
  --row:#e6ecf6;
}
*{box-sizing:border-box;margin:0;padding:0}
html,body{width:943px;height:1200px;overflow:hidden;background:var(--stage);font-family:"Source Sans 3",Arial,sans-serif}
.sheet{position:relative;width:943px;height:1200px}
.slide{position:absolute;width:283px;height:213px;overflow:hidden;background:linear-gradient(180deg,var(--paper-tint) 0,var(--paper) 28px,var(--paper) 100%)}
.c1{left:26px}.c2{left:332px}.c3{left:638px}
.r1{top:29px}.r2{top:262px}.r3{top:494px}.r4{top:726px}.r5{top:958px}

/* content slide chrome */
.content::before{content:"";position:absolute;right:-30px;bottom:-58px;width:200px;height:78px;border-radius:50%;background:linear-gradient(90deg,#a9c6ea,var(--brand) 45%,var(--brand-deep));}
.content::after{content:"";position:absolute;left:-20px;bottom:-50px;width:220px;height:66px;border-radius:50%;background:var(--paper)}
.orb{position:absolute;left:8px;top:8px;width:13px;height:13px;border-radius:50%;background:radial-gradient(circle at 35% 35%,#fff 0,#8fbbe9 30%,var(--brand) 75%)}
.slide-title{position:absolute;left:28px;top:7px;font-size:10px;font-weight:400;color:var(--title);line-height:13px}
.foot-logo{position:absolute;left:18px;bottom:10px;z-index:2;color:var(--brand);font-size:7.5px;font-weight:600;line-height:8px}
.foot-url{position:absolute;left:80px;bottom:12px;z-index:2;font-size:3.5px;color:var(--muted)}
.page-no{position:absolute;right:9px;bottom:5px;z-index:2;font-size:3.5px;color:#fff}

.para{position:absolute;font-size:3.6px;line-height:4.6px;color:var(--ink);text-align:justify}
.para p{margin-bottom:3px}
.photo{position:absolute;border-radius:1px}
.photo.tower{background:linear-gradient(180deg,#1d2a45,#6a7da3 60%,#c9a36a)}
.photo.people{background:linear-gradient(135deg,#d9c3a8,#8a6e58 60%,#e8e4dc)}
.photo.round{border-radius:50%;background:linear-gradient(160deg,#e7d2bf,#9a7a66 70%,#f0ece8)}

/* numbered list */
.item{position:absolute;width:180px}
.item .num{position:absolute;left:0;top:1px;width:13px;height:13px;border-radius:50%;background:radial-gradient(circle at 35% 35%,#9bc2ee,var(--brand-light) 60%,var(--brand));color:#fff;font-size:3.5px;text-align:center;line-height:13px}
.item h4{margin-left:20px;font-size:4.2px;font-weight:700;color:var(--ink);line-height:5px}
.item p{margin-left:20px;font-size:3.5px;line-height:4.4px;color:var(--ink)}
.item.narrow{width:90px}

.caption{position:absolute;width:50px;text-align:center;font-size:3.5px;line-height:4.4px;color:var(--ink)}
.caption b{display:block;font-size:4px}

/* blue slides */
.blue{background:linear-gradient(180deg,#3f7ccb 0,var(--brand) 45%,var(--brand-deep) 100%)}
.blue svg.base{position:absolute;left:0;bottom:0}
.hero-title{position:absolute;left:0;width:100%;text-align:center;color:#fff;font-size:16px;font-weight:400}
.hero-sub{position:absolute;left:0;width:100%;text-align:center;color:var(--accent);font-size:4.8px;font-weight:700;letter-spacing:.2px}
.blue-url{position:absolute;left:120px;top:5px;font-size:3.5px;color:#d8e6f7}
.wordmark{position:absolute;color:var(--brand);font-weight:600;line-height:1}
.portrait{position:absolute;width:25px;height:31px;background:linear-gradient(180deg,#c9b8a8,#3b4250);border:1px solid #fff}
.presenter{position:absolute;font-size:3px;line-height:4px;color:var(--ink);text-align:right}

/* cover */
.cover{background:var(--paper)}
.cover svg{position:absolute;left:0;top:0}
.address{position:absolute;right:14px;bottom:12px;font-size:3.2px;line-height:4px;color:var(--brand);text-align:right}

/* bullets */
.bullets{position:absolute;left:152px;top:52px;list-style:none;font-size:4.2px;line-height:8.4px;color:var(--ink)}
.bullets li::before{content:"";display:inline-block;width:4px;height:4px;border-radius:50%;background:var(--bullet);margin-right:5px;vertical-align:middle}

/* tables */
.data{position:absolute;border-collapse:collapse;font-size:3.5px;color:var(--ink)}
.data th{background:var(--brand);color:#fff;font-weight:600;text-align:left;padding:2px 3px}
.data td{padding:2.2px 3px}
.data tr:nth-child(odd) td{background:var(--row)}
.data td:first-child{color:var(--brand)}
.legend{position:absolute;font-size:2.8px;color:var(--muted)}
.map{position:absolute;left:24px;top:50px;width:236px;height:110px;background:radial-gradient(ellipse at 30% 40%,#c6d3e4,#dfe7f1 60%,transparent 75%),radial-gradient(ellipse at 70% 45%,#c6d3e4,#e6ecf4 55%,transparent 72%)}
</style>
</head>
<body>
<main class="sheet">

<!-- Cover -->
<section class="slide cover c1 r1">
  <svg width="283" height="213" viewBox="0 0 283 213">
    <defs><linearGradient id="coverSky" x1="0" y1="0" x2="0" y2="1"><stop offset="0" stop-color="#4a86d2"/><stop offset="1" stop-color="#1f4f9c"/></linearGradient></defs>
    <path d="M0 0H283V95C200 70 110 68 0 98Z" fill="url(#coverSky)"/>
    <path d="M0 98C110 68 200 70 283 95V100C200 78 110 76 0 106Z" fill="#cfe0f3"/>
  </svg>
  <div class="blue-url">www.arclinemedia.com</div>
  <div class="wordmark" style="left:100px;top:124px;font-size:22px">Arcline</div>
  <div class="address">Arcline Headquarters<br>120 Harbor Row<br>Suite 400, Eastfield CA 90210</div>
</section>

<!-- Title slide -->
<section class="slide blue c2 r1">
  <div class="hero-title" style="top:78px">Presentation Tittle Here</div>
  <div class="hero-sub" style="top:100px">YOUR PRESENTATION SUB TITLE HERE</div>
  <svg class="base" width="283" height="60" viewBox="0 0 283 60">
    <path d="M0 22C90 4 190 4 283 18V60H0Z" fill="#bcd4ef"/>
    <path d="M0 28C90 10 190 10 283 24V60H0Z" fill="#fff"/>
  </svg>
  <div class="wordmark" style="left:20px;bottom:12px;font-size:9px">Arcline</div>
  <div class="presenter" style="right:42px;bottom:8px">Presenter: Alex Moreno<br>Marketing Manager</div>
  <div class="portrait" role="img" aria-label="Presenter portrait photo" style="right:10px;bottom:6px"></div>
</section>

<!-- Slide 1 -->
<section class="slide content c3 r1">
  <div class="orb"></div><h2 class="slide-title">Arcline Slide Presentation 1</h2>
  <div class="photo tower" role="img" aria-label="Photo of a glass office tower at dusk" style="left:33px;top:38px;width:62px;height:76px"></div>
  <div class="para" style="left:150px;top:38px;width:100px">
    <p>The team has forged a bold and dynamic approach to audience research, overcoming pitfalls that held the industry back. The team has pushed the frontier of media insight to a new level.</p>
    <p>Central to this approach are proven pitfalls that held the industry back. The team has pushed the frontier of data research to a new level, launching initiatives that reshaped how brand research and campaign planning are done today.</p>
    <p>The pace at which learning and new ideas can be brought to clients.</p>
  </div>
  <div class="foot-logo">Arcline</div><div class="foot-url">www.arclinemedia.com</div><div class="page-no">1</div>
</section>

<!-- Slide 2 -->
<section class="slide content c1 r2">
  <div class="orb"></div><h2 class="slide-title">Arcline Slide Presentation 2</h2>
  <div class="photo people" role="img" aria-label="Photo of a smiling team of colleagues" style="left:28px;top:38px;width:62px;height:38px"></div>
  <div class="para" style="left:28px;top:88px;width:62px">
    <p>The team has forged a bold and dynamic approach to audience research.</p>
    <p>By overcoming proven pitfalls that held the industry back, the team has pushed the frontier of media research to a new level.</p>
    <p>The frontier of data research to a new level.</p>
  </div>
  <div class="para" style="left:150px;top:38px;width:100px">
    <p>The team has forged a bold and dynamic approach to audience research. By overcoming proven pitfalls that held the industry back, the team has pushed the frontier of media research to a new level and set the pace for insight.</p>
    <p>Central to this approach are proven pitfalls that held the industry back. The team has pushed the frontier of data research to a new level, launching initiatives that reshaped campaign planning.</p>
    <p>The industry back, the team has pushed the frontier of data research to a new level.</p>
  </div>
  <div class="foot-logo">Arcline</div><div class="foot-url">www.arclinemedia.com</div><div class="page-no">2</div>
</section>

<!-- Slide 3 -->
<section class="slide content c2 r2">
  <div class="orb"></div><h2 class="slide-title">Arcline Slide Presentation 3</h2>
  <div class="item" style="left:28px;top:36px"><span class="num">1</span><h4>We know firsthand 1</h4><p>Since 1998, we have supported thousands of brands from the point of discovery through their journey with the market.</p></div>
  <div class="item" style="left:28px;top:62px"><span class="num">2</span><h4>We know firsthand 2</h4><p>Since 1998, we have supported thousands of brands from the point of discovery through their journey with the market, we have supported thousands of brands.</p></div>
  <div class="item" style="left:28px;top:88px"><span class="num">3</span><h4>We know firsthand 3</h4><p>Since 1998, we have supported thousands of brands from the point of discovery through their journey with the market, we have supported thousands of brands.</p></div>
  <div class="item" style="left:28px;top:114px"><span class="num">4</span><h4>We know firsthand 2</h4><p>Since 1998, we have supported thousands of brands from the point of discovery through their journey with the market, we have supported thousands of brands from the point of discovery.</p></div>
  <div class="foot-logo">Arcline</div><div class="foot-url">www.arclinemedia.com</div><div class="page-no">3</div>
</section>

<!-- Slide 4 -->
<section class="slide content c3 r2">
  <div class="orb"></div><h2 class="slide-title">Arcline Slide Presentation 4</h2>
  <div class="item narrow" style="left:28px;top:36px"><span class="num">1</span><h4>We know firsthand 1</h4><p>Since 1998, we have supported thousands of brands from the point of discovery through their journey.</p></div>
  <div class="item narrow" style="left:28px;top:70px"><span class="num">2</span><h4>We know firsthand 2</h4><p>Since 1998, we have supported thousands of brands from the point of discovery.</p></div>
  <div class="item narrow" style="left:28px;top:98px"><span class="num">3</span><h4>We know firsthand 3</h4><p>Since 1998, we thousands of brands from the point of discovery.</p></div>
  <div class="item narrow" style="left:148px;top:36px"><span class="num">4</span><h4>We know firsthand 4</h4><p>Since 1998, we have supported thousands of brands through their journey with the market.</p></div>
  <div class="item narrow" style="left:148px;top:70px"><span class="num">5</span><h4>We know firsthand 5</h4><p>Since 1998, we have supported thousands of brands from the point of discovery.</p></div>
  <div class="foot-logo">Arcline</div><div class="foot-url">www.arclinemedia.com</div><div class="page-no">4</div>
</section>

<!-- Slide 5 -->
<section class="slide content c1 r3">
  <div class="orb"></div><h2 class="slide-title">Arcline Slide Presentation 5</h2>
  <div class="photo round" role="img" aria-label="Round photo of a smiling woman on the phone" style="left:38px;top:36px;width:42px;height:42px"></div>
  <div class="photo round" role="img" aria-label="Round photo of a hand touching a screen" style="left:108px;top:36px;width:42px;height:42px;background:linear-gradient(160deg,#f2f4f6,#b9c2cc 60%,#e9edf1)"></div>
  <div class="photo round" role="img" aria-label="Round photo of a support agent with headset" style="left:178px;top:36px;width:42px;height:42px"></div>
  <div class="caption" style="left:34px;top:88px"><b>Full Gala in Eastfield</b>Annual event brought together over two hundred guests and clients for a night of ideas.</div>
  <div class="caption" style="left:104px;top:88px"><b>Full Gala in Eastfield</b>Annual event brought together guests and clients.</div>
  <div class="caption" style="left:174px;top:88px"><b>Full Gala in Eastfield</b>Annual event brought together over two hundred guests and clients.</div>
  <div class="foot-logo">Arcline</div><div class="foot-url">www.arclinemedia.com</div><div class="page-no">5</div>
</section>

<!-- Map slide -->
<section class="slide content c2 r3">
  <div class="orb"></div><h2 class="slide-title" style="width:195px">More Than 500+ Satisfied Client Over All the World</h2>
  <div class="map" role="img" aria-label="World map with client locations marked"></div>
  <div class="foot-logo">Arcline</div><div class="foot-url">www.arclinemedia.com</div><div class="page-no">6</div>
</section>

<!-- Divider -->
<section class="slide blue c3 r3">
  <div class="blue-url">www.arclinemedia.com</div>
  <div class="hero-title" style="top:72px">Divider Pages Here</div>
  <div class="hero-sub" style="top:94px">PRESENTATION SUB TITLE HERE</div>
  <svg class="base" width="283" height="80" viewBox="0 0 283 80">
    <path d="M40 80C120 60 210 30 283 14V80Z" fill="#bcd4ef"/>
    <path d="M60 80C130 64 215 38 283 24V80Z" fill="#fff"/>
  </svg>
  <div class="wordmark" style="left:190px;bottom:22px;font-size:9px">Arcline</div>
  <div class="page-no" style="color:var(--brand)">7</div>
</section>

<!-- Slide 7 -->
<section class="slide content c1 r4">
  <div class="orb"></div><h2 class="slide-title">Arcline Slide Presentation 7</h2>
  <svg style="position:absolute;left:22px;top:46px" width="110" height="90" viewBox="0 0 110 90">
    <ellipse cx="55" cy="45" rx="54" ry="42" fill="#8b9097"/>
    <ellipse cx="62" cy="51" rx="44" ry="34" fill="#b5bac1"/>
    <ellipse cx="67" cy="56" rx="35" ry="27" fill="#5d8fd0"/>
    <ellipse cx="71" cy="61" rx="26" ry="20" fill="#2f63b0"/>
    <ellipse cx="74" cy="68" rx="17" ry="13" fill="#1c4690"/>
    <g fill="#fff" font-size="3.6" font-weight="700" text-anchor="middle" font-family="Source Sans 3, sans-serif">
      <text x="70" y="12">BRIEF</text><text x="70" y="26">ANALYZE</text><text x="71" y="39">DESIGN</text><text x="72" y="53">DEVELOP</text><text x="74" y="70">TESTING</text>
    </g>
  </svg>
  <ul class="bullets" style="top:44px">
    <li>Since 1998, we have supported</li><li>Essential to this approach various</li><li>Pitfalls that held the industry</li><li>Since 1998, we have supported</li><li>Essential to this approach various</li><li>Pitfalls that held the industry</li><li>Text has propelled the frontier</li><li>Multiple platforms research to</li><li>Since 1998, we have supported</li><li>Essential to this approach various</li>
  </ul>
  <div class="foot-logo">Arcline</div><div class="foot-url">www.arclinemedia.com</div><div class="page-no">9</div>
</section>

<!-- Slide 8 pie -->
<section class="slide content c2 r4">
  <div class="orb"></div><h2 class="slide-title">Arcline Slide Presentation 8</h2>
  <div class="para" style="left:28px;top:40px;width:100px">
    <p>The team has forged a bold and dynamic approach to audience research, overcoming pitfalls that held the industry back. The team has pushed the frontier of media research to a new level.</p>
    <p>Essential to this approach are proven pitfalls that held the industry back. The team has pushed the frontier of data research to a new level, launching initiatives that have reshaped campaign planning and brand development. With these models, the team can rapidly grow the pace at which learning and new ideas can be brought to clients.</p>
  </div>
  <svg style="position:absolute;left:138px;top:48px" width="120" height="80" viewBox="0 0 120 80">
    <ellipse cx="60" cy="42" rx="52" ry="30" fill="#1c4690"/>
    <ellipse cx="60" cy="36" rx="52" ry="30" fill="#3a70c2"/>
    <path d="M60 36L60 6A52 30 0 0 0 12 48Z" fill="#9aa1aa"/>
    <path d="M60 36L12 48A52 30 0 0 0 40 64Z" fill="#c4c9cf"/>
    <path d="M60 36L40 64A52 30 0 0 0 58 66Z" fill="#6d747d"/>
  </svg>
  <div class="legend" style="left:150px;top:136px">■ Area 1 &nbsp; ■ Area 2 &nbsp; ■ Area 3 &nbsp; ■ Area 4</div>
  <div class="foot-logo">Arcline</div><div class="foot-url">www.arclinemedia.com</div><div class="page-no">10</div>
</section>

<!-- Slide 9 columns -->
<section class="slide content c3 r4">
  <div class="orb"></div><h2 class="slide-title">Arcline Slide Presentation 9</h2>
  <div class="para" style="left:28px;top:40px;width:100px">
    <p>The team has forged a bold and dynamic approach to audience research, overcoming pitfalls that held the industry back. The team has pushed the frontier of media research to a new level.</p>
    <p>Essential to this approach are proven pitfalls that held the industry back. The team has pushed the frontier of data research to a new level, launching initiatives that have reshaped campaign planning and brand development. With these models, the team can rapidly grow the pace at which learning and new ideas can be brought to clients.</p>
  </div>
  <svg style="position:absolute;left:140px;top:50px" width="120" height="82" viewBox="0 0 120 82">
    <path d="M8 80L20 72H112L100 80Z" fill="#e1e5ea"/>
    <g>
      <rect x="14" y="60" width="14" height="20" fill="#aeb4bb"/><path d="M14 60l5-4h14l-5 4zM28 60l5-4v20l-5 4z" fill="#d0d4d9"/>
      <rect x="36" y="42" width="14" height="38" fill="#2a5ca8"/><path d="M36 42l5-4h14l-5 4zM50 42l5-4v38l-5 4z" fill="#5a8ed2"/>
      <rect x="58" y="30" width="14" height="50" fill="#1e4a94"/><path d="M58 30l5-4h14l-5 4zM72 30l5-4v50l-5 4z" fill="#4b80c8"/>
      <rect x="80" y="14" width="14" height="66" fill="#2d62b0"/><path d="M80 14l5-4h14l-5 4zM94 14l5-4v66l-5 4z" fill="#6a9bd9"/>
    </g>
  </svg>
  <div class="legend" style="left:146px;top:138px">■ Area 1 &nbsp; ■ Area 2 &nbsp; ■ Area 3 &nbsp; ■ Area 4</div>
  <div class="foot-logo">Arcline</div><div class="foot-url">www.arclinemedia.com</div><div class="page-no">11</div>
</section>

<!-- Slide 9 table -->
<section class="slide content c1 r5">
  <div class="orb"></div><h2 class="slide-title">Arcline Slide Presentation 9</h2>
  <div class="para" style="left:28px;top:40px;width:90px">
    <p>The team has forged a bold and dynamic approach to audience research, overcoming pitfalls that held the industry back. The team has pushed the frontier of media research to a new level.</p>
    <p>Essential to this approach are proven pitfalls that held the industry back. The team has pushed the frontier of data research to a new level, launching initiatives that reshaped campaign planning. With these models, the team can rapidly grow the pace at which new ideas reach clients.</p>
  </div>
  <table class="data" style="left:134px;top:40px;width:124px">
    <tr><th>No</th><th>Name</th><th>Date</th><th>Case</th></tr>
    <tr><td>01.</td><td>Ms Dana Keller</td><td>17-06-15</td><td>Open</td></tr>
    <tr><td>02.</td><td>Mrs Sarah Lane</td><td>17-06-15</td><td>Open</td></tr>
    <tr><td>03.</td><td>Ms Dana Keller</td><td>17-06-15</td><td>Close</td></tr>
    <tr><td>04.</td><td>Mrs Sarah Lane</td><td>17-06-15</td><td>Open</td></tr>
    <tr><td>05.</td><td>Ms Dana Keller</td><td>17-06-15</td><td>Open</td></tr>
    <tr><td>06.</td><td>Mrs Sarah Lane</td><td>17-06-15</td><td>Close</td></tr>
    <tr><td>07.</td><td>Ms Dana Keller</td><td>17-06-15</td><td>Close</td></tr>
    <tr><td>08.</td><td>Mrs Sarah Lane</td><td>17-06-15</td><td>Open</td></tr>
  </table>
  <div class="foot-logo">Arcline</div><div class="foot-url">www.arclinemedia.com</div><div class="page-no">12</div>
</section>

<!-- Slide 8 table -->
<section class="slide content c2 r5">
  <div class="orb"></div><h2 class="slide-title">Arcline Slide Presentation 8</h2>
  <table class="data" style="left:28px;top:38px;width:228px">
    <tr><th>No</th><th>Name</th><th>Id Case</th><th>Address</th><th>Date</th><th>Case</th></tr>
    <tr><td>01.</td><td>Ms Dana Keller</td><td>021396</td><td>Hall Street 13a</td><td>17-06-15</td><td>Open</td></tr>
    <tr><td>02.</td><td>Mrs Sarah Lane</td><td>021396</td><td>Adora Street 14a</td><td>17-06-15</td><td>Open</td></tr>
    <tr><td>03.</td><td>Ms Dana Keller</td><td>021396</td><td>Village Street 14a</td><td>17-06-15</td><td>Close</td></tr>
    <tr><td>04.</td><td>Mrs Sarah Lane</td><td>021396</td><td>Harbor Street 14a</td><td>17-06-15</td><td>Open</td></tr>
    <tr><td>05.</td><td>Ms Dana Keller</td><td>021396</td><td>Hall Street 14a</td><td>17-06-15</td><td>Open</td></tr>
  </table>
  <div class="para" style="left:28px;top:118px;width:228px">
    <p>The team has forged a bold and dynamic approach to audience research, overcoming pitfalls that held the industry back. The team has pushed the frontier of media research to a new level.</p>
    <p>Essential to this approach are proven pitfalls that held the industry back. The team has pushed the frontier of data research to a new level with bold initiatives.</p>
  </div>
  <div class="foot-logo">Arcline</div><div class="foot-url">www.arclinemedia.com</div><div class="page-no">13</div>
</section>

<!-- Thank you -->
<section class="slide blue c3 r5">
  <div class="hero-title" style="top:80px">Thank You Very Much</div>
  <div class="hero-sub" style="top:102px">YOUR PRESENTATION SUB TITLE HERE</div>
  <svg class="base" width="283" height="60" viewBox="0 0 283 60">
    <path d="M0 22C90 4 190 4 283 18V60H0Z" fill="#bcd4ef"/>
    <path d="M0 28C90 10 190 10 283 24V60H0Z" fill="#fff"/>
  </svg>
  <div class="wordmark" style="left:20px;bottom:12px;font-size:9px">Arcline</div>
  <div class="presenter" style="right:42px;bottom:8px">Presenter: Alex Moreno<br>Marketing Manager</div>
  <div class="portrait" role="img" aria-label="Presenter portrait photo" style="right:10px;bottom:6px"></div>
</section>

</main>
</body>
</html>
```